Web App Dashboard Design for Healthcare Company

We have developed a simple web application with 3 navigation menus. We like the current design (very much modeled after Ledgerly), but we want to explore UI options for the branding, header, menus, and footer that we may not have considered.

The attached screenshots show the layout and two menu "hover" views as they currently exist.

This web application is used by employees only.

Menu 1 - Module Menu:
Allows the user to switch easily between Account, Employee, and Care Management.

Menu 2 - Reports Menu
Allows user to view available reports within each Module.

Menu 3 - Admin Menu
Allows the user to easily create new content types within each module.

Use our branded colors and font.

Colors:
Logo Blue (dark): 00c0f3
Logo Blue (light): 44c8f5
Nav Blue: 0994d0
Green: 71b44b
Grayscale: (not specified)

Font:
Lato (Google Font)

Target Market(s)

Internal staff.

Industry/Entity Type

Healthcare

Number of Pages Required

3 page

Font styles to use
Sans Serif
Other font styles liked:
• Lato (Google Font)

Colors
0293ce
9bcb3c

Requirements
Must have
• It's really a one page design, but we want to see the two "hover" views for the Module Menu and the Admin Menu.
• It should also be very clear which "Report" page the user is on (the active menu link).
• Must use branded colors, font, and logo.
• Logo Blue (dark): 00c0f3
• Logo Blue (light): 44c8f5
• Nav Blue: 0994d0
• Green: 71b44b
• Grayscale: Designer may choose
Nice to have
• It would be nice to have simple uncluttered payouts.
Should not have
• The design should not have menu options exposed by default.

```html
<!DOCTYPE html>
<html lang="en">
<head>
<meta charset="utf-8">
<title>CareTally – Reports</title>
<link href="https://fonts.googleapis.com/css2?family=Lato:wght@300;400;700&display=swap" rel="stylesheet">
<style>
:root{
  --sidebar:#27313b;
  --sidebar-line:#35404b;
  --sidebar-text:#e6ebef;
  --sidebar-muted:#8e9aa6;
  --page:#eef1f2;
  --panel:#ffffff;
  --line:#e6e9eb;
  --text:#3b4248;
  --muted:#9aa3aa;
  --cyan:#00c0e0;
  --green:#8bc34a;
  --blue:#1e88d6;
  --purple:#a765de;
  --nav-blue:#0994d0;
  --btn-blue:#2a8ee0;
  --yellow:#f9c20a;
  --red:#e52a2a;
  --badge-green:#2bb44a;
  --badge-cyan:#0ab0e8;
  --row-alt:#f7f8f9;
  --chart-purple:#dbbdee;
  --chart-blue:#8ea8e3;
  --chart-green:#8cc185;
  --side-gray:#e5e9ec;
}
*{box-sizing:border-box;margin:0;padding:0}
html,body{width:1200px;height:821px;overflow:hidden}
body{font-family:'Lato',sans-serif;color:var(--text);background:var(--page);position:relative;font-size:9px}
.abs{position:absolute}

/* sidebar */
.sidebar{position:absolute;left:0;top:0;width:126px;height:821px;background:var(--sidebar)}
.brand{position:absolute;left:30px;top:12px;display:flex;align-items:center;gap:5px}
.brand-mark{width:12px;height:12px;background:var(--cyan)}
.brand-name{font-size:14px;font-weight:700;color:var(--cyan)}
.nav-label{position:absolute;left:12px;top:49px;font-size:9px;color:var(--sidebar-muted)}
.nav-item{position:absolute;left:12px;width:104px;height:14px;display:flex;align-items:center;color:var(--sidebar-text);font-size:8.5px}
.nav-item svg{width:9px;height:9px;margin-right:11px;fill:#c9d1d8}
.nav-item .badge{position:absolute;right:10px;width:12px;height:12px;border-radius:50%;font-size:7px;color:#fff;display:flex;align-items:center;justify-content:center}
.nav-item .chev{position:absolute;right:0;color:#aab4bd;font-size:9px}
.nav-sep{position:absolute;left:0;top:204px;width:126px;height:1px;background:var(--sidebar-line)}

/* header */
.topbar{position:absolute;left:126px;top:0;width:1074px;height:35px;background:#fff;border-bottom:1px solid var(--line)}
.topbar .item{position:absolute;top:0;height:35px;display:flex;align-items:center;font-size:8.5px;color:var(--text)}
.search-pill{position:absolute;left:194px;top:9px;width:117px;height:18px;border-radius:9px;background:#f1f3f4;font-size:8px;color:#b4bbc1;padding-left:9px;display:flex;align-items:center}
.dot-badge{position:absolute;width:9px;height:9px;border-radius:50%;background:var(--red);color:#fff;font-size:6px;display:flex;align-items:center;justify-content:center}
.avatar-photo{border-radius:50%;background:linear-gradient(135deg,#c98d6c,#6b4a3b)}

/* page title */
.title-band{position:absolute;left:126px;top:35px;width:924px;height:50px;border-bottom:1px solid #e1e5e7;background:#f3f5f6}
.page-title{position:absolute;left:16px;top:13px;font-size:12.5px;color:var(--text)}
.page-sub{position:absolute;left:16px;top:29px;font-size:7.5px;color:#c3c9ce;letter-spacing:.3px}

/* stat cards */
.stat{position:absolute;top:103px;width:163px;height:68px;color:#fff;text-align:center;overflow:hidden}
.stat .num{position:absolute;left:0;right:0;top:14px;font-size:25px;font-weight:300}
.stat .cap{position:absolute;left:0;right:0;top:45px;font-size:7px;opacity:.85}
.stat svg{position:absolute;left:0;bottom:0;width:163px;height:14px}
.stat-cyan{left:144px;background:var(--cyan)}
.stat-green{left:326px;background:var(--green)}
.stat-blue{left:508px;background:var(--blue)}
.stat-purple{left:690px;background:var(--purple)}

/* panels */
.panel{position:absolute;background:var(--panel)}
.reports-panel{left:144px;top:186px;width:891px;height:390px}
.panel-title{position:absolute;left:15px;top:9px;font-size:11.5px;color:var(--text)}
.rule{position:absolute;left:0;width:100%;height:1px;background:var(--line)}
.field{position:absolute;height:23px;border:1px solid #e1e5e8;background:#fff;font-size:8.5px;display:flex;align-items:center;padding-left:8px;color:var(--text)}
.table-head{position:absolute;top:107px;font-size:8.5px;font-weight:700;color:var(--text);letter-spacing:.2px}
.row{position:absolute;left:15px;width:861px;height:42px;border-top:1px solid var(--line)}
.row.alt{background:var(--row-alt)}
.row .check{position:absolute;left:13px;top:14px;width:13px;height:13px;border:1px solid #d7dbde;background:#fff}
.row .face{position:absolute;left:39px;top:7px;width:29px;height:29px}
.row .name{position:absolute;left:79px;top:15px;font-size:8.5px;color:var(--text)}
.row .content{position:absolute;left:208px;top:15px;font-size:8.5px;color:#5b6369}
.row .date{position:absolute;left:487px;top:15px;font-size:8.5px;color:#5b6369}
.row .module{position:absolute;left:657px;top:13px;width:46px;height:15px;color:#fff;font-size:8.5px;display:flex;align-items:center;justify-content:center}
.showing{position:absolute;left:15px;top:357px;font-size:8px;color:var(--muted)}
.pager{position:absolute;left:716px;top:352px;display:flex;border:1px solid #e1e5e8}
.pager span{width:23px;height:22px;display:flex;align-items:center;justify-content:center;font-size:8.5px;border-left:1px solid #e1e5e8;color:var(--text)}
.pager span:first-child{border-left:none}
.pager .on{background:#f1f3f4}

.services-panel{left:144px;top:594px;width:891px;height:212px}
.services-title{position:absolute;left:15px;top:13px;font-size:11.5px}
.services-sub{position:absolute;left:15px;top:33px;font-size:8px;color:var(--muted)}
.axis{position:absolute;left:12px;width:12px;text-align:right;font-size:8.5px;color:var(--text)}
.grid{position:absolute;left:35px;width:804px;height:1px;background:#eceff1}
.chart{position:absolute;left:35px;top:64px;width:660px;height:116px}
.side-stats{position:absolute;left:714px;top:0;width:177px;height:212px;background:var(--side-gray)}
.side-title{position:absolute;left:17px;top:13px;font-size:11.5px}
.bar-label{position:absolute;left:18px;font-size:8.5px;color:var(--text)}
.bar{position:absolute;left:18px;width:142px;height:3px;background:#fff;border-radius:2px}
.bar i{position:absolute;left:0;top:0;height:3px;border-radius:2px}
.side-copy{position:absolute;left:19px;top:166px;width:150px;font-size:8.5px;line-height:11px;color:#4d555b}

/* right panel */
.aside{position:absolute;left:1050px;top:35px;width:150px;height:786px;background:#fff;border-left:1px solid var(--line)}
.tab-line{position:absolute;left:0;top:48px;width:150px;height:1px;background:var(--line)}
.tab-active{position:absolute;left:0;top:47px;width:50px;height:2px;background:#3b4248}
.aside-h{position:absolute;left:17px;font-size:8.5px;font-weight:700;color:var(--text)}
.btn{position:absolute;left:16px;top:301px;width:118px;height:21px;background:var(--btn-blue);color:#fff;font-size:8.5px;display:flex;align-items:center;justify-content:center}
.todo{position:absolute;left:17px;display:flex;align-items:center;font-size:8.2px;color:var(--text)}
.box{width:8px;height:8px;border:1px solid #dfe3e6;margin-right:8px;display:flex;align-items:center;justify-content:center}
.box.done{background:var(--btn-blue);border-color:var(--btn-blue)}
.todo-input{position:absolute;left:16px;top:562px;width:86px;height:20px;border:1px solid #e1e5e8;font-size:8px;color:#b4bbc1;padding-left:7px;display:flex;align-items:center}
.todo-add{position:absolute;left:102px;top:562px;width:33px;height:20px;background:var(--btn-blue);color:#fff;font-size:9px;font-weight:700;display:flex;align-items:center;justify-content:center}
</style>
</head>
<body>

<aside class="sidebar">
  <div class="brand"><span class="brand-mark"></span><span class="brand-name">CareTally</span></div>
  <div class="nav-label">Navigation</div>
  <div class="nav-item" style="top:75px"><svg viewBox="0 0 10 10"><circle cx="5" cy="5" r="5"/></svg>Reminders<span class="badge" style="background:var(--badge-green)">2</span><span class="chev">›</span></div>
  <div class="nav-item" style="top:100px"><svg viewBox="0 0 10 10"><rect y="1.5" width="10" height="7"/></svg>Accounts</div>
  <div class="nav-item" style="top:124px"><svg viewBox="0 0 10 10"><rect y="1" width="10" height="9"/></svg>Patient Requests<span class="badge" style="background:var(--badge-cyan);right:-1px">5</span></div>
  <div class="nav-item" style="top:150px"><svg viewBox="0 0 10 10"><path d="M1 0h6l2 2v8H1z"/></svg>Reports<span class="badge" style="background:var(--yellow)">8</span><span class="chev">›</span></div>
  <div class="nav-item" style="top:175px"><svg viewBox="0 0 10 10"><rect width="4.5" height="4.5"/><rect x="5.5" width="4.5" height="4.5"/><rect y="5.5" width="4.5" height="4.5"/><rect x="5.5" y="5.5" width="4.5" height="4.5"/></svg>My Company<span class="chev">›</span></div>
  <div class="nav-sep"></div>
</aside>

<header class="topbar">
  <div class="item" style="left:23px"><svg width="11" height="9" viewBox="0 0 11 9"><rect width="11" height="1.5" fill="#3b4248"/><rect y="3.7" width="11" height="1.5" fill="#3b4248"/><rect y="7.5" width="11" height="1.5" fill="#3b4248"/></svg></div>
  <div class="item" style="left:53px"><svg width="9" height="9" viewBox="0 0 10 10" style="margin-right:5px"><circle cx="5" cy="3" r="2.6" fill="#3b4248"/><path d="M0 10c0-3 2-4.5 5-4.5s5 1.5 5 4.5z" fill="#3b4248"/></svg>Account Management&nbsp;&nbsp;▾</div>
  <div class="search-pill">Search projects...<svg class="abs" style="right:7px;top:5px" width="8" height="8" viewBox="0 0 8 8"><circle cx="3.3" cy="3.3" r="2.5" stroke="#8e979e" fill="none"/><path d="M5.2 5.2 7.5 7.5" stroke="#8e979e"/></svg></div>
  <div class="item" style="left:828px;color:#5b6369"><svg width="9" height="9" viewBox="0 0 10 10" style="margin-right:3px"><circle cx="5" cy="5" r="4" fill="none" stroke="#9aa3aa" stroke-width="2" stroke-dasharray="2 1.2"/></svg>Settings&nbsp;▾</div>
  <div class="item" style="left:899px"><svg width="11" height="11" viewBox="0 0 11 11"><rect x=".5" y="1.5" width="10" height="9" fill="none" stroke="#6a7379"/><path d="M.5 4h10M3 6h1M5 6h1M7 6h1M3 8h1M5 8h1M7 8h1" stroke="#6a7379"/></svg></div>
  <span class="dot-badge" style="left:906px;top:6px">5</span>
  <div class="item" style="left:940px"><svg width="10" height="11" viewBox="0 0 10 11"><path d="M5 1C2.8 1 2 2.8 2 5v2L.8 8.5h8.4L8 7V5C8 2.8 7.2 1 5 1z" fill="none" stroke="#6a7379"/><path d="M4 9.5a1 1 0 0 0 2 0" stroke="#6a7379" fill="none"/></svg></div>
  <span class="dot-badge" style="left:947px;top:6px">2</span>
  <div class="item" style="left:982px">My Info</div>
  <div class="item" style="left:1020px;font-size:7px">▼</div>
  <div class="abs avatar-photo" role="img" aria-label="User profile photo" style="left:1036px;top:8px;width:20px;height:20px"></div>
  <span class="abs" style="left:1051px;top:23px;width:6px;height:6px;border-radius:50%;background:var(--badge-green);border:1px solid #fff"></span>
</header>

<section class="title-band">
  <h1 class="page-title" style="font-weight:400">REPORTS</h1>
  <div class="page-sub">REPORTS STATISTIC</div>
</section>

<div class="stat stat-cyan"><div class="num">132</div><div class="cap">Contents Created</div><svg viewBox="0 0 163 14" preserveAspectRatio="none"><polyline points="0,11 15,9 28,12 40,8 55,11 68,7 82,10 95,6 110,10 124,8 138,11 150,7 163,10" fill="none" stroke="rgba(255,255,255,.35)" stroke-width="1"/></svg></div>
<div class="stat stat-green"><div class="num">18</div><div class="cap">Modules</div><svg viewBox="0 0 163 14" preserveAspectRatio="none"><polyline points="0,12 14,8 27,11 42,7 56,10 70,6 84,11 97,8 110,11 126,6 140,10 152,7 163,11" fill="none" stroke="rgba(255,255,255,.35)" stroke-width="1"/></svg></div>
<div class="stat stat-blue"><div class="num">25</div><div class="cap">Reports</div><svg viewBox="0 0 163 14" preserveAspectRatio="none"><polyline points="0,10 13,12 26,8 40,11 55,7 68,10 80,6 95,11 108,8 122,12 136,8 150,11 163,7" fill="none" stroke="rgba(255,255,255,.35)" stroke-width="1"/></svg></div>
<div class="stat stat-purple"><div class="num">3</div><div class="cap">In To Do list</div><svg viewBox="0 0 163 14" preserveAspectRatio="none"><polyline points="0,11 12,7 25,10 38,6 52,11 64,8 78,12 92,7 105,10 118,6 132,11 146,8 163,10" fill="none" stroke="rgba(255,255,255,.35)" stroke-width="1"/></svg></div>

<section class="panel reports-panel">
  <h2 class="panel-title" style="font-weight:400">Reports Table</h2>
  <svg class="abs" style="left:868px;top:12px" width="10" height="10" viewBox="0 0 10 10"><circle cx="5" cy="5" r="3.3" fill="none" stroke="#8e979e" stroke-width="2.4" stroke-dasharray="1.8 1"/><circle cx="5" cy="5" r="1.3" fill="#8e979e"/></svg>
  <div class="rule" style="top:31px"></div>
  <div class="field" style="left:16px;top:44px;width:113px">Bulk Action<span class="abs" style="right:8px;font-size:7px">▼</span></div>
  <div class="field" style="left:164px;top:44px;width:58px;justify-content:center;padding:0">Apply</div>
  <div class="field" style="left:735px;top:44px;width:119px;color:#5b6369">Search</div>
  <div class="field" style="left:853px;top:44px;width:24px;justify-content:center;padding:0">Go</div>
  <div class="rule" style="top:80px"></div>

  <div class="table-head" style="left:55px">NAME</div>
  <div class="table-head" style="left:223px">REPPORTS</div>
  <div class="table-head" style="left:502px">DATE</div>
  <div class="table-head" style="left:677px">MODULE</div>

  <div class="row alt" style="top:126px"><span class="check"></span><span class="face avatar-photo" role="img" aria-label="Profile photo of Shaunta Pollan"></span><span class="name">Shaunta Pollan</span><span class="content">content 1 title here</span><span class="date">Jul 25, 2015</span><span class="module" style="background:#1275c8">Module 1</span></div>
  <div class="row" style="top:168px"><span class="check"></span><span class="face avatar-photo" role="img" aria-label="Profile photo of Ronald Reck" style="background:linear-gradient(135deg,#e8cf9e,#a7b9cf)"></span><span class="name">Ronald Reck</span><span class="content">content 2 title here</span><span class="date">Jul 25, 2015</span><span class="module" style="background:var(--yellow)">Module 2</span></div>
  <div class="row alt" style="top:210px"><span class="check"></span><span class="face avatar-photo" role="img" aria-label="Profile photo of Kristine Spindler" style="background:linear-gradient(135deg,#9aa6ad,#4a3d36)"></span><span class="name">Kristine Spindler</span><span class="content">content 3 title here</span><span class="date">Jul 25, 2015</span><span class="module" style="background:#7cc142">Module 3</span></div>
  <div class="row" style="top:252px"><span class="check"></span><span class="face avatar-photo" role="img" aria-label="Profile photo of Randolph Seckman" style="background:linear-gradient(135deg,#e7ecee,#c9b6a8)"></span><span class="name">Randolph Seckman</span><span class="content">content 4 title here</span><span class="date">Jul 25, 2015</span><span class="module" style="background:var(--purple)">Module 4</span></div>
  <div class="row alt" style="top:294px;border-bottom:1px solid var(--line)"><span class="check"></span><span class="face avatar-photo" role="img" aria-label="Profile photo of Bailey Angell" style="background:linear-gradient(135deg,#d9c1b2,#2b2320)"></span><span class="name">Bailey Angell</span><span class="content">content 5 title here</span><span class="date">Jul 25, 2015</span><span class="module" style="background:var(--red)">Module 5</span></div>

  <div class="showing">Showing 20-30 of 50 items</div>
  <div class="pager"><span>«</span><span>1</span><span class="on">2</span><span>3</span><span>4</span><span>5</span><span>»</span></div>
</section>

<section class="panel services-panel">
  <h2 class="services-title" style="font-weight:400">Managed Services</h2>
  <div class="services-sub">Service report of this year (updated 1 hour ago)</div>
  <div class="axis" style="top:59px">80</div>
  <div class="axis" style="top:88px">60</div>
  <div class="axis" style="top:117px">40</div>
  <div class="axis" style="top:146px">20</div>
  <div class="axis" style="top:174px">0</div>
  <div class="grid" style="top:64px;width:660px"></div>
  <div class="grid" style="top:93px;width:660px"></div>
  <div class="grid" style="top:122px;width:660px"></div>
  <div class="grid" style="top:151px;width:660px"></div>
  <svg class="chart" viewBox="0 0 660 116" preserveAspectRatio="none">
    <path fill="var(--chart-purple)" d="M0,116 L0,40 20,30 40,22 60,28 80,36 100,26 120,32 140,24 160,18 180,26 200,14 220,4 240,10 260,6 280,16 300,12 320,26 340,20 360,34 380,46 400,40 420,44 440,36 460,42 480,30 500,44 520,38 540,32 560,40 580,34 600,46 620,38 640,44 660,30 L660,116Z"/>
    <path fill="var(--chart-blue)" d="M0,116 L0,55 20,48 40,52 60,45 80,58 100,50 120,56 140,48 160,52 180,46 200,40 220,50 240,44 260,52 280,48 300,58 320,62 340,56 360,66 380,70 400,64 420,60 440,58 460,66 480,54 500,62 520,58 540,64 560,56 580,68 600,60 620,66 640,58 660,70 L660,116Z"/>
    <path fill="var(--chart-green)" d="M0,116 L0,105 20,100 40,102 60,96 80,100 100,98 120,104 140,100 160,96 180,100 200,102 220,98 240,100 260,104 280,100 300,96 320,92 340,88 360,84 380,90 400,86 420,80 440,84 460,90 480,86 500,92 520,88 540,90 560,84 580,92 600,96 620,100 640,98 660,104 L660,116Z"/>
  </svg>
  <div class="side-stats">
    <h3 class="side-title" style="font-weight:400">Reports</h3>
    <div class="bar-label" style="top:54px">Consulting</div>
    <div class="bar" style="top:67px"><i style="width:92px;background:var(--chart-blue)"></i></div>
    <div class="bar-label" style="top:92px">Online tutorials</div>
    <div class="bar" style="top:104px"><i style="width:63px;background:var(--chart-green)"></i></div>
    <div class="bar-label" style="top:130px">EDU management</div>
    <div class="bar" style="top:143px"><i style="width:40px;background:var(--chart-purple)"></i></div>
    <p class="side-copy">Lorem ipsum dolor sit amet, consect adipisicing elit, sed do eiusmod por incididunt ut labore et dolore</p>
  </div>
</section>

<aside class="aside">
  <div class="tab-line"></div><div class="tab-active"></div>
  <div class="aside-h" style="top:67px">My Notes</div>
  <div class="btn">Add New Note</div>
  <div class="rule" style="top:340px"></div>
  <div class="aside-h" style="top:358px;left:16px">Todo List</div>
  <div class="abs" style="left:16px;top:374px;font-size:8px;color:#b4bbc1">3 of 5 remaining</div>
  <div class="todo" style="top:399px"><span class="box done"><svg width="6" height="6" viewBox="0 0 6 6"><path d="M1 3 2.5 4.5 5 1.5" stroke="#fff" fill="none" stroke-width="1.2"/></svg></span>Add New content</div>
  <div class="todo" style="top:430px"><span class="box"></span>Creating component page</div>
  <div class="todo" style="top:460px"><span class="box done"><svg width="6" height="6" viewBox="0 0 6 6"><path d="M1 3 2.5 4.5 5 1.5" stroke="#fff" fill="none" stroke-width="1.2"/></svg></span>Change Password</div>
  <div class="todo" style="top:490px"><span class="box done"><svg width="6" height="6" viewBox="0 0 6 6"><path d="M1 3 2.5 4.5 5 1.5" stroke="#fff" fill="none" stroke-width="1.2"/></svg></span>Create new Module</div>
  <div class="todo" style="top:521px"><span class="box"></span>Update my account</div>
  <div class="todo-input">Add new todo</div>
  <div class="todo-add">Add</div>
</aside>

</body>
</html>
```